Book cover for a very impressive real-life healing story from a stage IV deadly disease

I need a book cover design for the French translation of the US book http://www.pagevendo.com/Tims-Journey-Fever-Outlasted-Illness/dp/0845512097/ref=sr_1_4?s=books&ie=UTF8&qid=1455100794&sr=1-4&keywords=kit+marsh
.
I do not want the word AIDS on the French cover, as the story of this book applies to any disease.

The french title will be something like :
Un nouveau matin !
Condamné par la médecine, il guérit grâce au jeûne, la détoxination, et l’amour.

which means something like
A new morning!
Subtitle : Given up by official medecine, he managed to heal with fasting, detox and love.

Many thanks !

Target Market(s)

Anybody interested in natural health

Requirements
Must have
• Nothing special
Nice to have
• Nothing special
Should not have
• Nothing special

```html
<!DOCTYPE html>
<html lang="fr">
<head>
<meta charset="utf-8">
<title>Un nouveau matin ! — couverture</title>
<link rel="stylesheet" href="https://fonts.googleapis.com/css2?family=Playfair+Display:wght@900&family=Roboto+Condensed:wght@700&display=swap">
<style>
  :root {
    --stage: #e4e4e4;
    --paper: #f1e8d5;
    --paper-edge: #d9c8a6;
    --paper-stain: #cdb68c;
    --title-red: #a8262a;
    --subtitle-ink: #2f3135;
    --wash-deep: #5f7f99;
    --wash-mid: #8fa7ba;
    --wash-light: #c3d0d9;
  }
  * { margin: 0; padding: 0; box-sizing: border-box; }
  html, body {
    width: 882px;
    height: 1200px;
    overflow: hidden;
    background: var(--stage);
  }
  .wraparound {
    position: absolute;
    top: 350px;
    left: 0;
    width: 882px;
    height: 500px;
    overflow: hidden;
    background:
      radial-gradient(ellipse 60% 55% at 62% 35%, var(--paper) 50%, transparent 100%),
      radial-gradient(ellipse 25% 25% at 5% 8%, var(--paper-stain) 0%, transparent 70%),
      radial-gradient(ellipse 20% 22% at 97% 10%, var(--paper-stain) 0%, transparent 70%),
      var(--paper-edge);
  }
  .watercolor-wash {
    position: absolute;
    left: 0;
    bottom: 0;
    width: 882px;
    height: 240px;
  }
  .back-cover {
    position: absolute;
    top: 0; left: 0;
    width: 368px;
    height: 500px;
  }
  .spine {
    position: absolute;
    top: 0;
    left: 368px;
    width: 44px;
    height: 500px;
  }
  .spine-title {
    position: absolute;
    top: 84px;
    left: 44px;
    transform-origin: 0 0;
    transform: rotate(90deg);
    white-space: nowrap;
    font-family: "Playfair Display", Georgia, serif;
    font-weight: 900;
    font-size: 19px;
    line-height: 20px;
    color: var(--title-red);
    text-transform: uppercase;
    text-align: center;
  }
  .front-cover {
    position: absolute;
    top: 0;
    left: 412px;
    width: 470px;
    height: 500px;
  }
  .title-block {
    position: absolute;
    top: 62px;
    left: 0;
    width: 100%;
    text-align: center;
  }
  .book-title {
    font-family: "Playfair Display", Georgia, serif;
    font-weight: 900;
    font-size: 44px;
    line-height: 1.08;
    color: var(--title-red);
    text-transform: uppercase;
  }
  .book-subtitle {
    margin-top: 44px;
    font-family: "Roboto Condensed", "Arial Narrow", sans-serif;
    font-weight: 700;
    font-size: 19px;
    line-height: 1.3;
    color: var(--subtitle-ink);
  }
</style>
</head>
<body>
  <main class="wraparound">
    <svg class="watercolor-wash" role="img" aria-label="Lavis d'aquarelle bleu-gris sur le bas de la couverture" viewBox="0 0 882 240" preserveAspectRatio="none">
      <defs>
        <filter id="wash-blur" x="-20%" y="-30%" width="140%" height="160%">
          <feGaussianBlur stdDeviation="18"/>
        </filter>
        <linearGradient id="wash-fade" x1="0" y1="0" x2="0" y2="1">
          <stop offset="0" stop-color="var(--wash-light)" stop-opacity="0"/>
          <stop offset="0.4" stop-color="var(--wash-light)" stop-opacity="0.6"/>
          <stop offset="1" stop-color="var(--wash-mid)" stop-opacity="0.9"/>
        </linearGradient>
      </defs>
      <rect x="0" y="0" width="882" height="240" fill="url(#wash-fade)"/>
      <g filter="url(#wash-blur)">
        <ellipse cx="150" cy="120" rx="200" ry="40" fill="var(--wash-mid)" opacity="0.7"/>
        <ellipse cx="520" cy="100" rx="240" ry="35" fill="var(--wash-light)" opacity="0.8"/>
        <ellipse cx="760" cy="170" rx="220" ry="50" fill="var(--wash-deep)" opacity="0.65"/>
        <ellipse cx="260" cy="210" rx="260" ry="45" fill="var(--wash-deep)" opacity="0.6"/>
        <ellipse cx="520" cy="200" rx="160" ry="30" fill="var(--wash-mid)" opacity="0.6"/>
      </g>
    </svg>

    <section class="back-cover" aria-label="Quatrième de couverture"></section>

    <section class="spine" aria-label="Dos du livre">
      <p class="spine-title">Un nouveau<br>matin !</p>
    </section>

    <section class="front-cover">
      <header class="title-block">
        <h1 class="book-title">Un nouveau<br>matin !</h1>
        <p class="book-subtitle">Condamné par la médecine<br>il guérit grâce au jeûne<br>la détoxination<br>et l'amour</p>
      </header>
    </section>
  </main>
</body>
</html>
```